Stationery for a private security company, "Brennock Security Services Ltd."

Needed is a stationery design for a private security company. The designs must show professionalism and that our company mean nothing but business. Watermark of the company logo on the letterhead page is also a must. The final design must represent innovation and professionalism. It would be great if designers could integrate the colours black and silver onto the cards and letterheads..

Thank you

```html
<!DOCTYPE html>
<html lang="en">
<head>
<meta charset="utf-8">
<title>Brennock Security Services Ltd. — Stationery</title>
<link href="https://fonts.googleapis.com/css2?family=Roboto+Condensed:wght@400;700&display=swap" rel="stylesheet">
<style>
:root{
  --stage:#8e8e8e;
  --ink:#0b0b0b;
  --paper:#ffffff;
  --silver:#b9b9b9;
  --silver-dark:#8a8a8a;
  --watermark:#ececec;
  --watermark-dark:#3a3a3a;
  --umber:#231a17;
}
*{box-sizing:border-box;margin:0;padding:0}
html,body{width:1200px;height:1000px;overflow:hidden}
body{background:var(--stage);position:relative;font-family:"Roboto Condensed",Arial,sans-serif;color:var(--ink)}
.piece{position:absolute;overflow:hidden;background:var(--paper)}
.piece.dark{background:var(--ink);color:var(--paper)}
.wave{position:absolute;left:0;width:100%}
.brand{font-weight:700;text-transform:uppercase;line-height:1;letter-spacing:.04em}
.brand .sub{display:block;letter-spacing:.02em}
.brand-mark{display:inline-block;width:10px;height:10px;background:currentColor;margin-right:6px;vertical-align:middle}
.watermark{position:absolute;font-weight:700;text-transform:uppercase;letter-spacing:.05em;color:var(--watermark);white-space:nowrap}
.person{position:absolute;font-weight:700}
.person .role{display:block;font-weight:400;font-size:8px;margin-top:2px}
.contacts{position:absolute;list-style:none;font-size:8px;line-height:10.5px}
.contacts li{display:flex;align-items:center;gap:4px}
.icon{display:inline-block;width:7px;height:7px;border-radius:1.5px;background:currentColor;flex:none}
.footer-row{position:absolute;display:flex;gap:28px;font-size:6px;align-items:center}
.footer-row span{display:flex;align-items:center;gap:5px}
</style>
</head>
<body>

<!-- Business card back, dark -->
<section class="piece dark card-back-dark" style="left:19px;top:28px;width:330px;height:193px">
  <div class="watermark" style="left:-8px;top:118px;font-size:44px;color:var(--watermark-dark)">Brennock</div>
  <div class="person" style="left:154px;top:24px;font-size:14px">Marcus Ellery<span class="role">Managing Director</span></div>
  <ul class="contacts" style="left:154px;top:104px;color:var(--paper)">
    <li><i class="icon"></i>+0 508.615.2290</li>
    <li><i class="icon"></i>+0 508.615.2290</li>
    <li><i class="icon"></i>+0 508.615.2290</li>
    <li><i class="icon"></i>office@brennocksecure.com</li>
    <li><i class="icon"></i>www.brennocksecure.com</li>
    <li><i class="icon"></i>14 Harbour Lane, Kestrel Bay, WA, 6391</li>
  </ul>
</section>

<!-- Business card front, dark -->
<section class="piece dark card-front-dark" style="left:373px;top:28px;width:330px;height:193px">
  <div class="brand" style="position:absolute;left:0;right:0;top:112px;text-align:center;font-size:28px">Brennock<span class="sub" style="font-size:12px;margin-top:5px">Security Services Ltd.</span></div>
</section>

<!-- Business card back, light -->
<section class="piece card-back-light" style="left:19px;top:238px;width:330px;height:193px">
  <div class="watermark" style="left:-8px;top:80px;font-size:44px">Brennock</div>
  <svg class="wave" style="bottom:0;height:50px" viewBox="0 0 330 50" preserveAspectRatio="none" aria-hidden="true">
    <path d="M0,24 C90,40 220,34 330,8 L330,14 C220,38 90,44 0,30 Z" fill="var(--silver)"/>
    <path d="M0,30 C90,44 220,40 330,14 L330,50 L0,50 Z" fill="var(--umber)"/>
  </svg>
  <div class="person" style="left:154px;top:24px;font-size:14px">Marcus Ellery<span class="role">Managing Director</span></div>
  <ul class="contacts" style="left:154px;top:83px">
    <li><i class="icon"></i>0 508.615.2290</li>
    <li><i class="icon"></i>0 508.615.2290</li>
    <li><i class="icon"></i>0 508.615.2290</li>
    <li><i class="icon"></i>office@brennocksecure.com</li>
    <li><i class="icon"></i>www.brennocksecure.com</li>
    <li><i class="icon"></i>14 Harbour Lane, Kestrel Bay, WA, 6391</li>
  </ul>
</section>

<!-- Business card front, light -->
<section class="piece card-front-light" style="left:373px;top:238px;width:330px;height:193px">
  <div class="brand" style="position:absolute;left:0;right:0;top:105px;text-align:center;font-size:26px">Brennock<span class="sub" style="font-size:11px;margin-top:5px">Security Services Ltd.</span></div>
  <svg class="wave" style="bottom:0;height:40px" viewBox="0 0 330 40" preserveAspectRatio="none" aria-hidden="true">
    <path d="M0,22 C100,4 220,10 330,6 L330,12 C220,16 100,10 0,26 Z" fill="var(--silver)"/>
    <path d="M0,26 C100,10 220,16 330,12 L330,40 L0,40 Z" fill="var(--ink)"/>
  </svg>
</section>

<!-- Letterhead -->
<section class="piece letterhead" style="left:721px;top:28px;width:457px;height:645px">
  <svg class="wave" style="top:0;height:40px" viewBox="0 0 457 40" preserveAspectRatio="none" aria-hidden="true">
    <path d="M0,0 H457 V22 C380,10 200,14 0,28 Z" fill="var(--ink)"/>
    <path d="M0,28 C200,14 380,10 457,22 L457,26 C380,16 200,20 0,34 Z" fill="var(--silver)"/>
  </svg>
  <div class="brand" style="position:absolute;left:40px;top:90px;font-size:15px">Brennock<span class="sub" style="font-size:7px;margin-top:2px">Security Services Ltd.</span></div>
  <ul class="contacts" style="left:308px;top:64px;font-size:6.5px;line-height:10px">
    <li><i class="icon" style="width:6px;height:6px"></i>0508.615.2290</li>
    <li><i class="icon" style="width:6px;height:6px"></i>office@brennocksecure.com</li>
    <li><i class="icon" style="width:6px;height:6px"></i>www.brennocksecure.com</li>
    <li><i class="icon" style="width:6px;height:6px"></i>14 Harbour Lane, Kestrel Bay, WA, 6391</li>
  </ul>
  <div class="watermark" style="left:72px;top:332px;font-size:70px">Brennock</div>
  <div style="position:absolute;left:0;right:0;bottom:6px;height:2px;background:var(--silver)"></div>
  <div style="position:absolute;left:0;right:0;bottom:0;height:4px;background:var(--ink)"></div>
</section>

<!-- Compliment slip -->
<section class="piece comp-slip" style="left:19px;top:449px;width:564px;height:259px">
  <svg class="wave" style="top:0;height:46px" viewBox="0 0 564 46" preserveAspectRatio="none" aria-hidden="true">
    <path d="M0,0 H564 V10 C440,18 200,20 0,30 Z" fill="var(--ink)"/>
    <path d="M0,30 C200,20 440,18 564,10 L564,14 C440,24 200,28 0,42 Z" fill="var(--silver)"/>
  </svg>
  <div class="brand" style="position:absolute;left:34px;top:102px;font-size:16px">Brennock<span class="sub" style="font-size:7px;margin-top:2px">Security Services Ltd.</span></div>
  <div style="position:absolute;left:32px;top:130px;font-size:6px">14 Harbour Lane, Kestrel Bay, WA, 6391</div>
  <div class="watermark" style="left:262px;top:145px;font-size:48px">Brennock</div>
  <div class="footer-row" style="left:32px;top:235px">
    <span><i class="icon" style="width:6px;height:6px"></i>0508.615.2290</span>
    <span><i class="icon" style="width:6px;height:6px"></i>office@brennocksecure.com</span>
    <span><i class="icon" style="width:6px;height:6px"></i>www.brennocksecure.com</span>
  </div>
  <div style="position:absolute;left:0;right:0;bottom:8px;height:2px;background:var(--silver)"></div>
  <div style="position:absolute;left:0;right:0;bottom:0;height:4px;background:var(--ink)"></div>
</section>

<!-- Envelope front -->
<section class="piece envelope-front" style="left:21px;top:721px;width:565px;height:259px">
  <svg class="wave" style="top:0;height:48px" viewBox="0 0 565 48" preserveAspectRatio="none" aria-hidden="true">
    <path d="M0,0 H565 V14 C440,22 200,22 0,30 Z" fill="var(--ink)"/>
    <path d="M0,30 C200,22 440,22 565,14 L565,18 C440,28 200,30 0,44 Z" fill="var(--silver)"/>
  </svg>
  <div class="brand" style="position:absolute;left:38px;top:82px;font-size:16px">Brennock<span class="sub" style="font-size:7px;margin-top:2px">Security Services Ltd.</span></div>
  <ul class="contacts" style="left:38px;top:124px;font-size:6.5px;line-height:11px">
    <li><i class="icon" style="width:6px;height:6px"></i>0508.615.2290</li>
    <li><i class="icon" style="width:6px;height:6px"></i>office@brennocksecure.com</li>
    <li><i class="icon" style="width:6px;height:6px"></i>www.brennocksecure.com</li>
    <li><i class="icon" style="width:6px;height:6px"></i>14 Harbour Lane, Kestrel Bay, WA, 6391</li>
  </ul>
  <div class="watermark" style="left:262px;top:120px;font-size:48px">Brennock</div>
  <div style="position:absolute;left:0;right:0;bottom:8px;height:2px;background:var(--silver)"></div>
  <div style="position:absolute;left:0;right:0;bottom:0;height:4px;background:var(--ink)"></div>
</section>

<!-- Envelope back -->
<section class="piece envelope-back" style="left:622px;top:724px;width:556px;height:255px">
  <div style="position:absolute;left:0;right:0;top:0;height:80px;background:var(--ink);border-radius:0 0 22px 22px"></div>
  <div class="brand" style="position:absolute;left:0;right:0;top:32px;text-align:center;font-size:14px;color:var(--paper)">Brennock</div>
</section>

</body>
</html>
```